Daniel Horvath Photography Business Card

I am a photographer in Philadelphia, PA. I have a business card that I have designed in Photoshop. This has been an ongoing process for me for far too long. I am 85% pleased with what I have. I need some experts like yourself who has that extra 25% to make this card 110%. I use the dots throughout my website as page/topic breaks. I also use the dots on the mailing side of my direct mail pieces.

Bluefield Printworks does my printing.
Their File Specs for a business card:
width - 3.625 inches
Height - 2.124 inches
@ 355 PPI or DPI
CMYK
1/8 inch Bleed/CUT
This is the size of my uploaded file samples

I will have the card printed on a 18 pt card stock - 4 color - 2 sides - with a matte coating

Tech Info: SIDE 01
For name DANIEL HORVATH : font choice is FoglihtenNo07 - size 14.4 - VA 150 - Text Height 140% - text width 130% - underlined - color is 30 - 30- 30 or (1e1e1e)
For word PHOTOGRAPHY : font choice is FoglihtenNo07 - size 6.4 - VA 360 - Text Height 200% - text width 270% - underlined - color is 162-162-162 or (a2a2a2)
For DOTS - font choice is FoglihtenNo07 - size 6.73 - VA 180 - Text Height 100% - text width 163% - color is 100-179-204 or (64b3cc) - blue dots / 1-1-1 or (010101) - Black dots
For DAN@DHORVATHSTUDIO.EXAMPLE - font choice is Helvetica Neue Light - size 4.55 - VA 121 - Text Height 200% - text width 132% - color is 1-1-1 or (010101)
For 555.418.7260 - font choice is Helvetica Neue Light - size 4.55 - VA 270 - Text Height 180% - text width 189% - color is 1-1-1 or (010101)
For DHORVATHSTUDIO.EXAMPLE - font choice is Helvetica Neue Light - size 9.1 - VA 180 - Text Height 150% - text width 130% - color is 133-192-214 or (85c0d6)

Tech Info: SIDE 02
not certain if it is my website address - DHORVATHSTUDIO.EXAMPLE - like the sample or
or my Logo with dots DANIEL HORVATH PHOTOGRAPHY, WITH UNDERLINEs AND DOTS JUST LIKE FIRST SIDE - MAYBE BIGGER
the name in Helvetica Neue Light - 255 pure white -
Dots are same colors as first side
The background color of choice - at least for now issssss: 84-91-99 or (545b63)

If you think you can make my card really say Wow! Please let me know. Thank you very much!

Target Market(s)

Ad Agencies

Industry/Entity Type

Professional Photography

Contact Information for Business Card

width - 3.625 inches
Height - 2.124 inches
@ 355 PPI or DPI
CMYK
1/8 inch Bleed/CUT

Tech Info: SIDE 01

Tech Info: SIDE 02

Font styles to use
Other font styles liked:
• FoglihtenNo07 and Helvetica Neue Light

Requirements
Must have
• I am a photographer in Philadelphia, PA. I have a business card that I have designed in Photoshop. This has been an ongoing process for me for far too long. I am 85% pleased with what I have. I need some experts like yourself who has that extra 25% to make this card 110%. I use the dots throughout my website as page/topic breaks. I also use the dots on the mailing side of my direct mail pieces.
• Bluefield Printworks does my printing.
• Their File Specs for a business card:
• width - 3.625 inches
• Height - 2.124 inches
• @ 355 PPI or DPI
• CMYK
• 1/8 inch Bleed/CUT
• This is the size of my uploaded file samples
• I will have the card printed on a 18 pt card stock - 4 color - 2 sides - with a matte coating
• Tech Info: SIDE 01
• For name DANIEL HORVATH : font choice is FoglihtenNo07 - size 14.4 - VA 150 - Text Height 140% - text width 130% - underlined - color is 30 - 30- 30 or (1e1e1e)
• For word PHOTOGRAPHY : font choice is FoglihtenNo07 - size 6.4 - VA 360 - Text Height 200% - text width 270% - underlined - color is 162-162-162 or (a2a2a2)
• For DOTS - font choice is FoglihtenNo07 - size 6.73 - VA 180 - Text Height 100% - text width 163% - color is 100-179-204 or (64b3cc) - blue dots / 1-1-1 or (010101) - Black dots
• For DAN@DHORVATHSTUDIO.EXAMPLE - font choice is Helvetica Neue Light - size 4.55 - VA 121 - Text Height 200% - text width 132% - color is 1-1-1 or (010101)
• For 555.418.7260 - font choice is Helvetica Neue Light - size 4.55 - VA 270 - Text Height 180% - text width 189% - color is 1-1-1 or (010101)
• For DHORVATHSTUDIO.EXAMPLE - font choice is Helvetica Neue Light - size 9.1 - VA 180 - Text Height 150% - text width 130% - color is 133-192-214 or (85c0d6)
• Tech Info: SIDE 02
• not certain if it is my website address - DHORVATHSTUDIO.EXAMPLE - like the sample or
• or my Logo with dots DANIEL HORVATH PHOTOGRAPHY, WITH UNDERLINEs AND DOTS JUST LIKE FIRST SIDE - MAYBE BIGGER
• the name in Helvetica Neue Light - 255 pure white -
• Dots are same colors as first side
• The background color of choice - at least for now issssss: 84-91-99 or (545b63)
• If you think you can make my card really say Wow! Please let me know. Thank you very much!
Nice to have
• I could really use some different sizes of the dots as a Vector file?? I use Photoshop for all my designs. Thank You.
Should not have
• all listed above

```html
<!DOCTYPE html>
<html lang="en">
<head>
<meta charset="utf-8">
<title>Daniel Horvath Photography – Business Card</title>
<link rel="stylesheet" href="https://fonts.googleapis.com/css2?family=Arimo:wght@400&family=Cormorant+Garamond:wght@500&display=swap">
<style>
  :root {
    --backdrop: #5bb9d4;
    --card: #f7f7f7;
    --ink: #1e1e1e;
    --black-dot: #1c1a1b;
    --accent: #06b2cf;
    --white: #ffffff;
    --serif: "Cormorant Garamond", "Times New Roman", serif;
    --sans: "Arimo", "Helvetica Neue", Arial, sans-serif;
  }
  * { margin: 0; padding: 0; box-sizing: border-box; }
  html, body { width: 1200px; height: 960px; overflow: hidden; }
  body { background: var(--backdrop); position: relative; }

  .card {
    position: absolute;
    left: 378px;
    width: 482px;
    height: 275px;
    background: var(--card);
  }
  .card--front { top: 150px; }
  .card--back  { top: 512px; }

  /* Front */
  .wordmark {
    position: absolute;
    font-family: var(--serif);
    font-weight: 500;
    color: var(--ink);
    text-align: center;
    line-height: 1;
  }
  .card--front .wordmark { left: 0; width: 100%; top: 68px; }
  .card--front .wordmark__name { font-size: 44px; letter-spacing: 0.5px; }
  .card--front .wordmark__field { font-size: 40px; letter-spacing: 1px; margin-top: 2px; }

  .front-url {
    position: absolute;
    left: 0; width: 100%;
    top: 157px;
    text-align: center;
    font-family: var(--sans);
    font-size: 17px;
    color: var(--ink);
  }

  .dot-row { position: absolute; left: 0; top: 0; }
  .dot { position: absolute; width: 19px; height: 19px; border-radius: 50%; top: 221px; }
  .dot--blue { background: var(--accent); }
  .dot--black { background: var(--black-dot); }

  /* Back */
  .card--back .wordmark { left: 38px; top: 36px; text-align: center; width: 200px; }
  .card--back .wordmark__name { font-size: 23px; }
  .card--back .wordmark__field { font-size: 22px; margin-top: 0; }

  .contact { position: absolute; left: 0; top: 0; }
  .contact__row { position: absolute; left: 34px; height: 22px; }
  .contact__icon {
    position: absolute; left: 0; top: 0;
    width: 21px; height: 21px; border-radius: 50%;
  }
  .contact__icon svg { display: block; width: 21px; height: 21px; }
  .contact__bar {
    position: absolute; left: 26px; top: 1px;
    height: 20px;
    border-radius: 2px 10px 10px 2px;
    font-family: var(--sans);
    font-size: 15px;
    line-height: 20px;
    color: var(--white);
    padding-left: 9px;
    white-space: nowrap;
  }
  .is-blue { background: var(--accent); }
  .is-black { background: var(--black-dot); }
</style>
</head>
<body>

<section class="card card--front" aria-label="Business card front">
  <div class="wordmark">
    <div class="wordmark__name">DANIEL HORVATH</div>
    <div class="wordmark__field">PHOTOGRAPHY</div>
  </div>
  <p class="front-url">WWW.DHORVATHSTUDIO.EXAMPLE</p>
  <div class="dot-row" aria-hidden="true">
    <span class="dot dot--blue"  style="left:20px"></span>
    <span class="dot dot--black" style="left:65px"></span>
    <span class="dot dot--blue"  style="left:102px"></span>
    <span class="dot dot--black" style="left:140px"></span>
    <span class="dot dot--blue"  style="left:178px"></span>
    <span class="dot dot--black" style="left:216px"></span>
    <span class="dot dot--blue"  style="left:255px"></span>
    <span class="dot dot--black" style="left:292px"></span>
    <span class="dot dot--blue"  style="left:331px"></span>
    <span class="dot dot--black" style="left:369px"></span>
    <span class="dot dot--blue"  style="left:407px"></span>
    <span class="dot dot--black" style="left:445px"></span>
  </div>
</section>

<section class="card card--back" aria-label="Business card back">
  <div class="wordmark">
    <div class="wordmark__name">DANIEL HORVATH</div>
    <div class="wordmark__field">PHOTOGRAPHY</div>
  </div>

  <div class="contact">
    <div class="contact__row" style="top:97px">
      <span class="contact__icon is-blue">
        <svg viewBox="0 0 21 21" aria-hidden="true">
          <circle cx="10.5" cy="7.5" r="3" fill="#fff"/>
          <path d="M5.5 16.5 a5 5 0 0 1 10 0 z" fill="#fff"/>
        </svg>
      </span>
      <span class="contact__bar is-blue" style="width:192px">DANIEL HORVATH</span>
    </div>

    <div class="contact__row" style="top:139px">
      <span class="contact__icon is-black">
        <svg viewBox="0 0 21 21" aria-hidden="true">
          <text x="10.5" y="15" text-anchor="middle" font-family="Arial, sans-serif" font-size="14" fill="#fff">@</text>
        </svg>
      </span>
      <span class="contact__bar is-black" style="width:290px">DAN@DHORVATHSTUDIO.EXAMPLE</span>
    </div>

    <div class="contact__row" style="top:179px">
      <span class="contact__icon is-blue">
        <svg viewBox="0 0 21 21" aria-hidden="true">
          <path d="M7 5 l2 3 -1.2 1.4 a7 7 0 0 0 3.8 3.8 L13 12 l3 2 -1.2 2 C10 16 5 11 5 6.2 Z" fill="#fff"/>
        </svg>
      </span>
      <span class="contact__bar is-blue" style="width:290px">555 418 7260</span>
    </div>

    <div class="contact__row" style="top:220px">
      <span class="contact__icon is-black">
        <svg viewBox="0 0 21 21" aria-hidden="true">
          <g fill="none" stroke="#fff" stroke-width="1">
            <circle cx="10.5" cy="10.5" r="6"/>
            <ellipse cx="10.5" cy="10.5" rx="2.6" ry="6"/>
            <line x1="4.5" y1="10.5" x2="16.5" y2="10.5"/>
            <line x1="5.5" y1="7.5" x2="15.5" y2="7.5"/>
            <line x1="5.5" y1="13.5" x2="15.5" y2="13.5"/>
          </g>
        </svg>
      </span>
      <span class="contact__bar is-black" style="width:290px">WWW.DHORVATHSTUDIO.EXAMPLE</span>
    </div>
  </div>
</section>

</body>
</html>
```